Business Card

I need a business card that really pops for a potential customer or person who refers a personal injury lead. I want to highlight our office locations, but only address that needs to be on the card is my office's main address. I want a sleek, modern and minimalist design.

```html
<!DOCTYPE html>
<html lang="en">
<head>
<meta charset="UTF-8">
<title>Northfield Injury Lawyers – Business Card</title>
<link href="https://fonts.googleapis.com/css2?family=Montserrat:wght@400;500;700;800&display=swap" rel="stylesheet">
<style>
  :root {
    --backdrop: #d4d7d7;
    --paper: #fbfbfa;
    --ink: #151515;
    --ink-soft: #3a3a3a;
    --card-dark: #2a2a2a;
    --foil: #f2f2f2;
  }
  * { margin: 0; padding: 0; box-sizing: border-box; }
  html, body {
    width: 1200px; height: 829px; overflow: hidden;
    background: var(--backdrop);
    font-family: "Montserrat", sans-serif;
  }
  .stage { position: relative; width: 1200px; height: 829px; }
  .card {
    position: absolute; top: 266px;
    width: 520px; height: 297px;
    box-shadow: 0 10px 24px rgba(0,0,0,0.18);
  }
  .card--front { left: 50px; background: var(--paper); }
  .card--back { left: 630px; background: var(--card-dark); }

  /* firm name placeholder */
  .firm-name {
    position: absolute; display: flex; align-items: center;
    font-weight: 500; line-height: 1; letter-spacing: 0; white-space: nowrap;
  }
  .firm-name__mark { flex: none; }
  .card--front .firm-name { left: 44px; top: 52px; gap: 10px; font-size: 20px; color: var(--ink); }
  .card--front .firm-name__mark { width: 14px; height: 14px; background: var(--ink); }
  .card--back .firm-name {
    left: 0; right: 0; top: 134px; justify-content: center;
    gap: 14px; font-size: 28px; color: var(--foil);
  }
  .card--back .firm-name__mark { width: 20px; height: 20px; background: var(--foil); }

  /* contact */
  .address {
    position: absolute; left: 44px; top: 118px;
    font-style: normal; font-size: 11.5px; line-height: 16px; color: var(--ink-soft);
  }
  .contact-list {
    position: absolute; left: 30px; top: 164px; list-style: none;
    font-size: 11.5px; line-height: 18px; color: var(--ink-soft);
  }
  .contact-list li { display: flex; align-items: center; gap: 5px; }
  .contact-list svg { width: 9px; height: 9px; fill: var(--ink); flex: none; }

  /* person */
  .person { position: absolute; right: 26px; top: 196px; text-align: right; }
  .person__name { font-size: 17px; font-weight: 800; color: var(--ink); letter-spacing: 0.6px; text-transform: uppercase; }
  .person__role { font-size: 11.5px; color: var(--ink-soft); margin-top: 3px; }
  .accent-bar {
    position: absolute; right: 0; top: 198px; width: 13px; height: 38px; background: var(--ink);
  }
</style>
</head>
<body>
<div class="stage">
  <section class="card card--front" aria-label="Card front">
    <div class="firm-name"><span class="firm-name__mark"></span>Northfield Injury Lawyers</div>
    <address class="address">2217 Linden Ave<br>Maple Grove, 24630</address>
    <ul class="contact-list">
      <li><svg viewBox="0 0 10 10"><path d="M2 0.5l1.6 2.2-1 1.1c0.6 1.3 1.5 2.2 2.7 2.8l1.1-1 2.1 1.6-0.8 2.1C4.4 9.2 0.8 5.6 0 2.2z"/></svg>(555) 284 3190</li>
      <li><svg viewBox="0 0 10 10"><path d="M0 2h10v6H0z M0.6 2.4l4.4 3.2 4.4-3.2" stroke="#fbfbfa" stroke-width="0.8"/></svg>hello@northfieldinjury.com</li>
      <li><svg viewBox="0 0 10 10"><circle cx="5" cy="5" r="4.6"/><path d="M0.6 5h8.8M5 0.5c-2.2 2.6-2.2 6.4 0 9M5 0.5c2.2 2.6 2.2 6.4 0 9" stroke="#fbfbfa" stroke-width="0.7" fill="none"/></svg>www.northfieldinjury.com</li>
    </ul>
    <div class="person">
      <p class="person__name">Daniel Harper</p>
      <p class="person__role">CEO/Founder</p>
    </div>
    <span class="accent-bar"></span>
  </section>

  <section class="card card--back" aria-label="Card back">
    <div class="firm-name"><span class="firm-name__mark"></span>Northfield Injury Lawyers</div>
  </section>
</div>
</body>
</html>
```